Business card design for Larkspire Bullion

I am looking for business card design concepts for my company, Larkspire Bullion. Please visit the website for more information www.larkspirebullion.example
I would like to use the logo you will see on the website.
I want a modern design that reflects the multi-thousand year history of precious metals use in the global economy. This is a very important subject that everyone needs to understand. I want the card to be classy and professional reflecting my personal commitment to the concept!

Target Market(s)

Individuals with funds to invest in precious metals.....gold,silver,etc.

Industry/Entity Type

Financial Service

Contact Information for Business Card

Should reflect the commitment to precious metals for everyone!

Font styles to use
Sans Serif

Colors
3276b5
0255a3

Requirements
Must have
• Logo, name: Tobias Renn, title: Owner, email address:tobias@larkspirebullion.example
• Phone numbers: Toll free 1-800-914-2057, local: 503-712-4193
• Website address: www.larkspirebullion.example, address: 2780 Quarry Lane SE, Portland, OR 97231
• Larger lettering for ease of reading (use both sides)
• "Precious Metals Expertise for Everyone" somewhere on the card!
Nice to have
• The color blue that matches the website blue.....
Should not have
• No black cards please.

```html
<!DOCTYPE html>
<html lang="en">
<head>
<meta charset="utf-8">
<title>Larkspire Bullion business card</title>
<link rel="stylesheet" href="https://fonts.googleapis.com/css2?family=Lato:wght@400;700&display=swap">
<style>
  :root {
    --blue: #3276b5;
    --blue-deep: #0255a3;
    --gold: #f0a93a;
    --ink: #1c1c1c;
    --rule: #6d6d6d;
    --paper: #ffffff;
    --backdrop: #e4e5e8;
  }
  * { box-sizing: border-box; margin: 0; padding: 0; }
  html, body { width: 1200px; height: 900px; overflow: hidden; }
  body {
    background: var(--backdrop);
    font-family: "Lato", sans-serif;
    position: relative;
  }
  .card {
    position: absolute;
    left: 260px;
    width: 680px;
    height: 388px;
    box-shadow: 0 6px 18px rgba(0,0,0,0.18);
    overflow: hidden;
  }
  .card--front { top: 40px; background: var(--blue); }
  .card--back { top: 472px; background: var(--paper); }

  .front-brand {
    position: absolute;
    top: 138px; left: 0; right: 0;
    text-align: center;
    color: var(--gold);
    font-weight: 700;
    font-size: 46px;
    letter-spacing: 2px;
    text-transform: uppercase;
  }
  .front-tagline {
    position: absolute;
    top: 232px; left: 0; right: 0;
    text-align: center;
    color: var(--paper);
    font-size: 20px;
    letter-spacing: 0.5px;
  }

  .back-brand {
    position: absolute;
    top: 46px; left: 56px;
    color: var(--gold);
    font-weight: 700;
    font-size: 32px;
    letter-spacing: 1.5px;
    text-transform: uppercase;
  }
  .person {
    position: absolute;
    top: 118px; right: 70px;
    text-align: right;
  }
  .person-name {
    color: var(--blue);
    font-weight: 700;
    font-size: 32px;
    line-height: 1.1;
  }
  .person-title {
    color: var(--ink);
    font-size: 20px;
    margin-top: 2px;
  }
  .divider {
    position: absolute;
    top: 196px; left: 56px; right: 70px;
    height: 1.5px;
    background: var(--rule);
  }
  .contacts {
    position: absolute;
    top: 212px; left: 56px;
    list-style: none;
  }
  .contacts li {
    display: flex;
    align-items: center;
    gap: 12px;
    color: var(--ink);
    font-size: 18px;
    line-height: 27px;
  }
  .contacts svg { width: 16px; height: 16px; flex: none; fill: var(--blue); }
  .address {
    position: absolute;
    right: 70px; bottom: 38px;
    text-align: right;
    color: var(--ink);
    font-size: 22px;
    line-height: 1.3;
  }
  .edge-band {
    position: absolute;
    left: 0; right: 0; bottom: 0;
    height: 10px;
    display: flex;
  }
  .edge-band .gold { flex: 1; background: var(--gold); }
  .edge-band .blue { flex: 1; background: var(--blue); }
</style>
</head>
<body>
  <section class="card card--front">
    <div class="front-brand">Larkspire Bullion</div>
    <p class="front-tagline">Precious Metals Expertise for Everyone</p>
  </section>

  <section class="card card--back">
    <div class="back-brand">Larkspire Bullion</div>
    <div class="person">
      <div class="person-name">Tobias Renn</div>
      <div class="person-title">Owner</div>
    </div>
    <div class="divider"></div>
    <ul class="contacts">
      <li>
        <svg viewBox="0 0 16 16" aria-hidden="true"><path d="M4 1l2.5 3-1.5 2c1 2 2.5 3.5 4.5 4.5l2-1.5 3 2.5-1.5 2.5C7 14 2 9 1.5 2.5z"/></svg>
        1-800-914-2057 (toll free)
      </li>
      <li>
        <svg viewBox="0 0 16 16" aria-hidden="true"><rect x="4" y="1" width="8" height="4"/><rect x="1" y="6" width="14" height="6" rx="1"/><rect x="4" y="10" width="8" height="5"/></svg>
        503-712-4193 (local)
      </li>
      <li>
        <svg viewBox="0 0 16 16" aria-hidden="true"><path d="M1 3h14v10H1z M1 3l7 6 7-6" fill="var(--blue)" stroke="#fff" stroke-width="1"/></svg>
        tobias@larkspirebullion.example
      </li>
      <li>
        <svg viewBox="0 0 16 16" aria-hidden="true"><circle cx="8" cy="8" r="7"/><path d="M1 8h14M8 1c-3 3-3 11 0 14M8 1c3 3 3 11 0 14" stroke="#fff" stroke-width="1" fill="none"/></svg>
        www.larkspirebullion.example
      </li>
    </ul>
    <address class="address" style="font-style:normal">
      2780 Quarry Lane SE<br>
      Portland, OR 97231
    </address>
    <div class="edge-band"><span class="gold"></span><span class="blue"></span></div>
  </section>
</body>
</html>
```